Zielgruppe
Strandhaus mit Restaurant (Beach feeling)
Zielgruppe: gehoben, edel, teuer
Aufgabenstellung
Auf stilsicherheit und das es stylisch und gleichzeitig edel aussieht.
Format:
Breite 44,5
Höher 71
Text:
Logo oben gut sichtbar
Herzlich Willkommen! (andere Schriftart)
MONTAG - FREITAG
SAMSTAG - SONNTAG
Unsere Küche verwöhnt dich bis 21:00 Uhr - täglich frisch & mit Liebe gekocht.
Wolkenhain ist mehr als ein Ort - es ist ein Gefühl. (andere Schriftart)
Lindenmoor, Kastner Weg 58-60, 2790 Talheim am See
www.wolkenhain-beispiel.at/reservieren

```html
<!DOCTYPE html>
<html lang="de">
<head>
<meta charset="utf-8">
<title>Wolkenhain – Öffnungszeiten</title>
<link rel="stylesheet" href="https://fonts.googleapis.com/css2?family=Montserrat:wght@500;600&family=Cabin:wght@400;500&family=Allura&display=swap">
<style>
  :root {
    --night: #0d1624;
    --sky: #3a8fd6;
    --sand: #e6ddc6;
  }
  html, body {
    margin: 0;
    padding: 0;
    overflow: hidden;
    background: var(--night);
  }
  .poster {
    position: relative;
    width: 800px;
    height: 1200px;
    overflow: hidden;
    background: radial-gradient(ellipse at 50% 40%, #111b2b 0%, var(--night) 70%);
    color: var(--sand);
    text-align: center;
  }
  .poster > * {
    position: absolute;
    left: 0;
    right: 0;
    margin: 0;
  }
  .brand-dot {
    top: 128px;
    left: 50%;
    right: auto;
    width: 22px;
    height: 22px;
    margin-left: -11px;
    border-radius: 50%;
    background: var(--sky);
  }
  .brand-name {
    top: 212px;
    font-family: "Montserrat", sans-serif;
    font-weight: 600;
    font-size: 52px;
    letter-spacing: 0.11em;
    line-height: 64px;
    color: var(--sky);
    padding-left: 0.11em;
  }
  .welcome {
    top: 318px;
    font-family: "Allura", cursive;
    font-weight: 400;
    font-size: 122px;
    line-height: 100px;
    color: var(--sand);
  }
  .hours {
    top: 545px;
    font-family: "Montserrat", sans-serif;
    font-weight: 600;
    color: var(--sand);
  }
  .hours-block {
    margin: 0 0 22px;
  }
  .hours-days {
    display: block;
    font-size: 29px;
    letter-spacing: 0.11em;
    line-height: 40px;
  }
  .hours-time {
    display: block;
    font-size: 29px;
    font-weight: 500;
    letter-spacing: 0.13em;
    line-height: 40px;
  }
  .kitchen-note {
    top: 752px;
    font-family: "Cabin", sans-serif;
    font-size: 27px;
    line-height: 35px;
    letter-spacing: 0.05em;
  }
  .tagline {
    top: 842px;
    font-family: "Allura", cursive;
    font-size: 74px;
    line-height: 66px;
  }
  .contact {
    top: 1072px;
    font-family: "Cabin", sans-serif;
    font-size: 26px;
    line-height: 35px;
    letter-spacing: 0.04em;
    font-style: normal;
  }
</style>
</head>
<body>
  <main class="poster">
    <div class="brand-dot" aria-hidden="true"></div>
    <h1 class="brand-name">WOLKENHAIN</h1>

    <h2 class="welcome">Herzlich<br>Willkommen!</h2>

    <section class="hours">
      <p class="hours-block">
        <span class="hours-days">MONTAG – FREITAG</span>
        <span class="hours-time">11:00 – 00:00</span>
      </p>
      <p class="hours-block">
        <span class="hours-days">SAMSTAG – SONNTAG</span>
        <span class="hours-time">09:00 – 00:00</span>
      </p>
    </section>

    <p class="kitchen-note">Unsere Küche verwöhnt dich bis 21:00 Uhr<br>– täglich frisch &amp; mit Liebe gekocht.</p>

    <p class="tagline">Wolkenhain ist mehr<br>als ein Ort – es ist ein<br>Gefühl.</p>

    <address class="contact">
      Lindenmoor, Kastner Weg 58–60,<br>
      2790 Talheim am See<br>
      www.wolkenhain-beispiel.at/reservieren
    </address>
  </main>
</body>
</html>
```